Personal development products that change your life

This is a direct selling business that sells personal development courses, but also sells the business as well if desired. This is not MLM, and there is no handling of the product required, nor hassling friends or family. We are looking for business minded people wanting to work their own hours and achieve a desirable income from this. A success image or happy image on a flyer would be great. I'd like the website address to be displayed as well thanks. www.sunpath-growvista.com.au

Target Market(s)

Business-minded individuals searching for more finances. Self motivated, driven, interested in self development.

Industry/Entity Type

Business

Font styles to use
Sans Serif

Requirements
Must have
• Are you looking for
• - a franchise or business?
• - a change of career?
• - a back up income?
• Not MLM
• No product handling or shipping
• No hard sales required
• website: www.sunpath-growvista.com.au
Nice to have
• A picture or background of excited person jumping in the air, or some similar.
• Worded to enrol people interested in achieving more financial headway, or flexible hours, or travel and do this business from anywhere in the world.
• Only need access to a phone, internet connection and a desire to succeed.

```html
<!DOCTYPE html>
<html lang="en">
<head>
<meta charset="utf-8">
<title>Sunpath Growvista flyer</title>
<link href="https://fonts.googleapis.com/css2?family=Roboto+Condensed:ital,wght@0,400;0,700;1,400;1,700;1,900&family=Roboto:wght@400;700;900&display=swap" rel="stylesheet">
<style>
  :root {
    --orange: #f07a1a;
    --orange-deep: #d85f0c;
    --sky-top: #2a1a14;
    --sky-glow: #f4962e;
    --sky-horizon: #ffcf6a;
    --ink: #141414;
    --panel-dark: #1c1c1c;
    --panel-mid: #3a3a3a;
    --band-light: #9a9a9a;
    --white: #ffffff;
    --muted: #e6e6e6;
  }
  * { margin: 0; padding: 0; box-sizing: border-box; }
  html, body { width: 874px; height: 1200px; overflow: hidden; background: #fff; }
  .flyer {
    position: relative;
    width: 874px; height: 1200px;
    overflow: hidden;
    background: radial-gradient(ellipse at 40% 70%, var(--panel-mid) 0%, var(--panel-dark) 70%, #0e0e0e 100%);
    font-family: "Roboto", Arial, sans-serif;
    color: var(--white);
  }
  .hero-photo {
    position: absolute; left: 0; top: 0; width: 874px; height: 400px;
    background: linear-gradient(180deg, var(--sky-top) 0%, #5a2c14 30%, var(--sky-glow) 68%, var(--sky-horizon) 80%, #3a2412 100%);
  }
  .title-band { position: absolute; left: 0; top: 330px; width: 874px; height: 300px; }
  .tagline {
    position: absolute; left: 110px; top: 393px; width: 700px;
    font-family: "Roboto Condensed", Arial, sans-serif; font-style: italic;
    font-size: 21px; color: var(--muted); transform: rotate(-3deg);
  }
  .brand-title {
    position: absolute; left: 60px; top: 418px; width: 780px; text-align: center;
    font-family: "Roboto Condensed", Arial, sans-serif; font-style: italic; font-weight: 900;
    font-size: 84px; line-height: 1; letter-spacing: 1px; color: var(--white);
    transform: rotate(-3deg);
  }
  .requirements {
    position: absolute; left: 55px; top: 530px; width: 790px;
    font-family: "Roboto Condensed", Arial, sans-serif; font-style: italic;
    font-size: 24px; line-height: 1.2; color: var(--white); transform: rotate(-3deg);
  }
  .question {
    position: absolute; left: 40px; top: 670px;
    font-size: 38px; font-weight: 700;
  }
  .options { position: absolute; left: 40px; top: 735px; list-style: none; }
  .options li {
    display: flex; align-items: center; gap: 14px;
    font-size: 33px; height: 50px;
  }
  .options svg { width: 34px; height: 34px; flex: none; }
  .balance-badge {
    position: absolute; left: 555px; top: 660px; width: 300px; height: 300px;
    border-radius: 50%;
    background: radial-gradient(circle at 50% 40%, #2a2a2a 0%, #111 75%);
    box-shadow: 0 0 0 3px #555, 0 6px 18px rgba(0,0,0,.6);
    display: flex; align-items: center; justify-content: center; text-align: center;
    font-size: 33px; line-height: 1.25; padding: 30px;
  }
  .perks { position: absolute; left: 0; top: 920px; list-style: none; }
  .perks li {
    display: block; margin-bottom: 12px;
    background: var(--orange); color: var(--white);
    font-size: 27px; font-weight: 400; line-height: 42px; height: 42px;
    padding: 0 22px 0 50px;
    clip-path: polygon(0 0, calc(100% - 14px) 0, 100% 50%, calc(100% - 14px) 100%, 0 100%);
  }
  .footer-rule {
    position: absolute; left: 0; top: 1088px; width: 874px; height: 6px;
    background: var(--orange);
  }
  .frame-side { position: absolute; top: 1088px; width: 10px; height: 112px; background: var(--orange); }
  .frame-left { left: 0; } .frame-right { right: 0; }
  .frame-bottom { position: absolute; left: 0; bottom: 0; width: 874px; height: 10px; background: var(--orange); }
  .website {
    position: absolute; left: 0; top: 1112px; width: 874px; text-align: center;
    font-size: 46px; font-weight: 700; color: var(--white);
  }
</style>
</head>
<body>
<main class="flyer">
  <div class="hero-photo" role="img" aria-label="Silhouettes of a group of people jumping joyfully against an orange sunset sky"></div>

  <svg class="title-band" viewBox="0 0 874 300" aria-hidden="true">
    <defs>
      <linearGradient id="metal" x1="0" y1="0" x2="0" y2="1">
        <stop offset="0" stop-color="#b5b5b5"/>
        <stop offset="0.5" stop-color="#6e6e6e"/>
        <stop offset="1" stop-color="#3e3e3e"/>
      </linearGradient>
    </defs>
    <polygon points="0,55 874,10 874,55 0,100" fill="#111"/>
    <polygon points="0,100 874,55 874,195 0,240" fill="url(#metal)" opacity="0.85"/>
    <polygon points="0,240 874,195 874,200 0,245" fill="#111"/>
  </svg>

  <p class="tagline">Ongoing personal development opportunities for successful applicants</p>
  <h1 class="brand-title">Sunpath Growvista</h1>
  <p class="requirements">All you need is a laptop, a phone,&nbsp; internet connection, a strong desire to succeed,&nbsp; and dedicate 15-20 hours per week</p>

  <h2 class="question">Are you looking for :</h2>
  <ul class="options">
    <li><svg viewBox="0 0 34 34"><circle cx="17" cy="17" r="15" fill="none" stroke="#fff" stroke-width="2.5"/><path d="M10 17l5 5 9-10" fill="none" stroke="#fff" stroke-width="3" stroke-linecap="round" stroke-linejoin="round"/></svg>a franchise or business?</li>
    <li><svg viewBox="0 0 34 34"><circle cx="17" cy="17" r="15" fill="none" stroke="#fff" stroke-width="2.5"/><path d="M10 17l5 5 9-10" fill="none" stroke="#fff" stroke-width="3" stroke-linecap="round" stroke-linejoin="round"/></svg>a change of career?</li>
    <li><svg viewBox="0 0 34 34"><circle cx="17" cy="17" r="15" fill="none" stroke="#fff" stroke-width="2.5"/><path d="M10 17l5 5 9-10" fill="none" stroke="#fff" stroke-width="3" stroke-linecap="round" stroke-linejoin="round"/></svg>a back up income?</li>
  </ul>

  <div class="balance-badge">Start the work / life balance you've always wanted</div>

  <ul class="perks">
    <li>Not MLM</li>
    <li>No hard sales required</li>
    <li>No product handling or shipping</li>
  </ul>

  <div class="footer-rule"></div>
  <div class="frame-side frame-left"></div>
  <div class="frame-side frame-right"></div>
  <div class="frame-bottom"></div>
  <p class="website">www.sunpath-growvista.com.au</p>
</main>
</body>
</html>
```